Master slides for standard ppt presentation

I just my company, went through Emblemyard for the log design and already have an identity that I like.
I need to transpose this identity into some nice Master slides for Powerpoint presentation. I want it clean, with fresh color connection to my logo, not over crowded and obviously different vs what powerpoint proposes as standard design ideas. I will attach a few materials that I already use, branded with the company logo so that you can take inspiration.

```html
<!DOCTYPE html>
<html lang="en">
<head>
<meta charset="utf-8">
<title>Veridune – Master Slides</title>
<link href="https://fonts.googleapis.com/css2?family=Montserrat:wght@400;500;600;700;800&display=swap" rel="stylesheet">
<style>
  :root{
    --teal-dark:#0d5a5c;
    --teal:#137476;
    --green:#27c07f;
    --green-soft:#5ed6a0;
    --ink:#1f2a2c;
    --muted:#5b6668;
    --page:#dfe5e8;
    --slide:#ffffff;
    --mist:#eef3f5;
  }
  *{box-sizing:border-box;margin:0;padding:0}
  html,body{width:1200px;height:4196px;overflow:hidden}
  body{background:var(--page);font-family:"Montserrat",Arial,sans-serif;color:var(--ink);position:relative}
  .slide{position:absolute;left:0;width:1200px;background:var(--slide);overflow:hidden}
  .slide::after{content:"";position:absolute;left:0;right:0;bottom:0;height:120px;z-index:0;
    background:linear-gradient(180deg,rgba(238,243,245,0),var(--mist));pointer-events:none}
  .slide > *{z-index:1}
  .abs{position:absolute}
  .photo{position:absolute;border-radius:2px}
  .warm{background:linear-gradient(135deg,#d8c7b4,#a9927e)}
  .cool{background:linear-gradient(135deg,#b7c8d6,#7d93a6)}
  .bright{background:linear-gradient(135deg,#e4ddd3,#b9a48f)}

  .slide-title{position:absolute;left:0;top:34px;padding-left:40px;border-left:12px solid var(--green);
    font-size:46px;font-weight:700;color:var(--teal-dark);line-height:56px}
  .brand-mark{position:absolute;right:40px;top:44px;display:flex;align-items:center;gap:12px;
    font-size:34px;font-weight:800;color:var(--teal-dark);letter-spacing:1px}
  .brand-mark .dot{width:30px;height:30px;border-radius:50%;background:var(--green)}
  .small{font-size:13px;line-height:19px;color:var(--muted)}

  .cover{top:0;height:680px;background:linear-gradient(180deg,#ffffff,var(--mist))}
  .cover .emblem{left:520px;top:90px;width:160px;height:160px;border-radius:50%;
    background:linear-gradient(135deg,var(--teal-dark),var(--green))}
  .cover .name{left:0;width:1200px;top:296px;text-align:center;font-size:64px;font-weight:800;color:var(--teal-dark);letter-spacing:3px}
  .cover .tagline{left:0;width:1200px;top:392px;text-align:center;font-size:38px;font-weight:700;color:var(--teal-dark)}
  .cover .sub{left:0;width:1200px;top:456px;text-align:center;font-size:20px;font-weight:500;color:var(--ink)}

  .story{top:712px;height:648px}
  .story .intro{left:52px;top:116px;width:880px}
  .story .lead{left:52px;top:166px;font-size:15px;font-weight:700}
  .story .photo{left:52px;top:212px;width:470px;height:380px}
  .story .statement{left:690px;top:252px;width:470px;font-size:27px;line-height:38px;color:var(--ink)}

  .promise{top:1400px;height:560px}
  .promise .subtitle{left:52px;top:108px;font-size:30px;font-weight:500}
  .promise .photo{top:166px;width:336px;height:240px}
  .promise .caption{top:424px;width:336px;font-size:20px;line-height:28px;font-weight:500}

  .what{top:2000px;height:780px}
  .what .body{left:52px;top:116px;width:530px}
  .what .photo.p1{left:52px;top:480px;width:256px;height:228px}
  .what .photo.p2{left:324px;top:480px;width:258px;height:228px}
  .what .photo.p3{left:612px;top:190px;width:540px;height:518px}

  .timeline{top:2800px;height:640px}
  .tl-svg{position:absolute;left:0;top:0}
  .tl-item{position:absolute;width:230px}
  .tl-item .year{font-size:32px;font-weight:800;color:var(--ink);line-height:38px}
  .tl-item .label{font-size:15px;font-weight:700;color:var(--green);margin:2px 0 6px}
  .tl-item .small{font-size:12px;line-height:16px}
  .tl-year-low{position:absolute;width:80px;text-align:right;font-size:30px;font-weight:800;color:var(--ink);line-height:36px}

  .thanks{top:3480px;height:716px;background:linear-gradient(180deg,#0f6b6d 0%,#149078 60%,#22b98a 100%)}
  .thanks::after{display:none}
  .thanks .emblem{left:530px;top:110px;width:140px;height:140px;border-radius:50%;background:rgba(255,255,255,.92)}
  .thanks .name{left:0;width:1200px;top:284px;text-align:center;font-size:62px;font-weight:800;color:#fff;letter-spacing:3px}
  .thanks .big{left:0;width:1200px;top:380px;text-align:center;font-size:120px;font-weight:800;color:#fff;letter-spacing:2px}
  .footer{position:absolute;left:40px;right:40px;bottom:28px;display:flex;align-items:center;color:#fff;font-size:18px}
  .footer .rule{width:150px;height:2px;background:#fff;margin:0 18px}
  .footer .soc{width:18px;height:18px;border-radius:50%;background:#fff;margin-right:10px}
  .footer .web{margin-left:auto}
</style>
</head>
<body>

<section class="slide cover">
  <div class="abs emblem"></div>
  <div class="abs name">VERIDUNE</div>
  <div class="abs tagline">We Create Value for Your Business</div>
  <div class="abs sub">Commercial Strategy - Negotiation - Business Modeling</div>
</section>

<section class="slide story">
  <h2 class="slide-title">Our Story</h2>
  <div class="brand-mark"><span class="dot"></span>VERIDUNE</div>
  <p class="abs intro small">Lorem ipsum dolor sit amet, consectetur adipiscing elit, sed do eiusmod tempor incididunt ut labore et dolore magna aliqua. Ut enim ad minim veniam, quis nostrud exercitation ullamco laboris nisi ut aliquip ex ea commodo consequat.</p>
  <p class="abs lead">Lorem ipsum dolor sit amet, consectetur adipiscing</p>
  <div class="photo warm" role="img" aria-label="Photo of a business team meeting around a laptop"></div>
  <p class="abs statement">After more than 30 years of cumulated experience in FMCG, we are now offering our expertise to companies willing to start a business in that area or looking for consultancy in order to improve results and increase profit.</p>
</section>

<section class="slide promise">
  <h2 class="slide-title">Our Promise</h2>
  <div class="brand-mark"><span class="dot"></span>VERIDUNE</div>
  <p class="abs subtitle">Nemo enim ipsam voluptatem quia voluptas</p>
  <div class="photo cool" style="left:72px" role="img" aria-label="Photo of hands reviewing charts on a desk"></div>
  <div class="photo bright" style="left:432px" role="img" aria-label="Photo of modern residential buildings"></div>
  <div class="photo warm" style="left:808px" role="img" aria-label="Photo of a handshake in a bright room"></div>
  <p class="abs caption" style="left:72px">Lorem ipsum dolor sit amet, consectetur adipiscing elit.</p>
  <p class="abs caption" style="left:432px">Lorem ipsum dolor sit amet, consectetur adipiscing elit,</p>
  <p class="abs caption" style="left:808px">Lorem ipsum dolor sit amet, consectetur adipiscing elit.</p>
</section>

<section class="slide what">
  <h2 class="slide-title">What we do</h2>
  <div class="brand-mark"><span class="dot"></span>VERIDUNE</div>
  <p class="abs body small">"Lorem ipsum dolor sit amet, consectetur adipiscing elit, sed do eiusmod tempor incididunt ut labore et dolore magna aliqua. Ut enim ad minim veniam, quis nostrud exercitation ullamco laboris nisi ut aliquip ex ea commodo consequat. "Lorem ipsum dolor sit amet, consectetur adipiscing elit, sed do eiusmod tempor incididunt ut labore et dolore magna aliqua. Ut enim ad minim veniam, quis nostrud exercitation ullamco laboris nisi ut aliquip ex ea commodo consequat. "Lorem ipsum dolor sit amet, consectetur adipiscing elit, sed do eiusmod tempor incididunt ut labore et dolore magna aliqua. Ut enim ad minim veniam, quis nostrud exercitation ullamco laboris nisi ut aliquip ex ea commodo consequat. "Lorem ipsum dolor sit amet, consectetur adipiscing elit, sed do eiusmod tempor incididunt ut labore et dolore magna aliqua.</p>
  <div class="photo p1 cool" role="img" aria-label="Photo of an engineer with a tablet on site"></div>
  <div class="photo p2 warm" role="img" aria-label="Photo of a smiling professional at an office"></div>
  <div class="photo p3 bright" role="img" aria-label="Photo of a consultant presenting plans to a couple"></div>
</section>

<section class="slide timeline">
  <h2 class="slide-title">Our Timeline</h2>
  <div class="brand-mark"><span class="dot"></span>VERIDUNE</div>
  <svg class="tl-svg" width="1200" height="640" viewBox="0 0 1200 640">
    <line x1="0" y1="400" x2="1200" y2="400" stroke="#137476" stroke-width="3"/>
    <g stroke="#137476" stroke-width="2" stroke-dasharray="4 5">
      <line x1="144" y1="250" x2="144" y2="358"/>
      <line x1="560" y1="250" x2="560" y2="358"/>
      <line x1="992" y1="250" x2="992" y2="358"/>
      <line x1="368" y1="434" x2="368" y2="486"/>
      <line x1="752" y1="434" x2="752" y2="486"/>
    </g>
    <g fill="#0d5a5c">
      <circle cx="144" cy="400" r="42"/><circle cx="560" cy="400" r="42"/><circle cx="992" cy="400" r="42"/>
    </g>
    <g fill="#27c07f">
      <circle cx="368" cy="400" r="34"/><circle cx="752" cy="400" r="34"/>
    </g>
    <g fill="none" stroke="#fff" stroke-width="3" stroke-linecap="round" stroke-linejoin="round">
      <circle cx="144" cy="400" r="10"/>
      <path d="M144 380v6M144 414v6M124 400h6M158 400h6M130 386l4 4M154 410l4 4M158 386l-4 4M130 414l4-4"/>
      <rect x="357" y="386" width="22" height="28" rx="2"/><path d="M362 395h12M362 402h12M362 409h8"/>
      <circle cx="556" cy="396" r="11"/><path d="M564 404l10 10"/>
      <path d="M738 388h28v18h-16l-8 7v-7h-4z"/>
      <path d="M981 387c3-2 6 0 7 3l1 4c0 2-2 3-3 4 2 5 5 8 10 10 1-1 2-3 4-3l4 1c3 1 5 4 3 7-2 3-5 4-8 3-11-3-18-10-21-21-1-3 0-6 3-8z"/>
    </g>
    <g fill="#137476">
      <circle cx="144" cy="250" r="4"/><circle cx="560" cy="250" r="4"/><circle cx="992" cy="250" r="4"/>
      <circle cx="368" cy="486" r="4"/><circle cx="752" cy="486" r="4"/>
    </g>
  </svg>
  <div class="tl-item" style="left:100px;top:130px">
    <div class="year">2017</div><div class="label">UT ENIM AD MINIMA</div>
    <p class="small">Lorem ipsum dolor sit amet, consectetur adipiscing elit, sed do eiusmod tempor incididunt ut labore.</p>
  </div>
  <div class="tl-item" style="left:516px;top:130px">
    <div class="year">2018</div><div class="label">UT ENIM AD MINIMA</div>
    <p class="small">Lorem ipsum dolor sit amet, consectetur adipiscing elit, sed do eiusmod tempor incididunt ut labore.</p>
  </div>
  <div class="tl-item" style="left:950px;top:130px">
    <div class="year">2019</div><div class="label">UT ENIM AD MINIMA</div>
    <p class="small">Lorem ipsum dolor sit amet, consectetur adipiscing elit, sed do eiusmod tempor incididunt ut labore.</p>
  </div>
  <div class="tl-year-low" style="left:278px;top:494px">2020</div>
  <div class="tl-item" style="left:380px;top:462px">
    <div class="label">UT ENIM AD MINIMA</div>
    <p class="small">Lorem ipsum dolor sit amet, consectetur adipiscing elit, sed do eiusmod tempor.</p>
  </div>
  <div class="tl-year-low" style="left:662px;top:494px">2023</div>
  <div class="tl-item" style="left:764px;top:462px">
    <div class="label">UT ENIM AD MINIMA</div>
    <p class="small">Lorem ipsum dolor sit amet, consectetur adipiscing elit, sed do eiusmod tempor.</p>
  </div>
</section>

<section class="slide thanks">
  <div class="abs emblem"></div>
  <div class="abs name">VERIDUNE</div>
  <div class="abs big">THANK YOU</div>
  <div class="footer">
    <span>Follow us</span><span class="rule"></span>
    <span class="soc"></span><span class="soc"></span><span class="soc"></span>
    <span class="web">www.veridune.com</span>
  </div>
</section>

</body>
</html>
```